Floral Waters needs a Label Design for bottles

Our products slogan: grown with water and sun.
Organic products of excellence originating from regions of extraordinary environmental quality, these products are the basis of natural cosmetics. Bio certificated and Organic.

We need a Luxury Label for the bottles of Floral Waters.
We don't want rustic, organic, rural, bio...
We want Luxury associated with environment.

The Label / decoration for the bottles must be editable, for we can change the titles of the floral Waters and information.
Elements :
Floral Water
Pet and Glass round Bottles Dimensions: 11cm Height , 4.5cm width
perimeter - 7.65
The logo is from tv lumora web store, it´s not necessary to include in the front of the paching design. it´s an open option

Target Market(s)

Medium High urban people , with ecologic and sustainable concerns. People who prefer natural and non Quimical cosmetics.

Industry/Entity Type

Floral

Requirements
Must have
• Sophisticated simple design
• Elements :
• Floral Water
• space for the name of the Floral Water ( ex: Salvia Officinalis, Minth, Melissa Officinalis)
• Grown with water and sun
Nice to have
• Variations of Gold
Should not have
• Bio, farm, organic, rustic,

```html
<!DOCTYPE html>
<html lang="en">
<head>
<meta charset="utf-8">
<title>Grown With Water and Sun – Floral Water Label</title>
<link rel="stylesheet" href="https://fonts.googleapis.com/css2?family=Ultra&family=Lobster&family=Cinzel:wght@600&family=Cormorant+Garamond:ital,wght@1,500&family=Nunito:wght@800&display=swap">
<style>
  :root {
    --frame-cyan: #21e6f2;
    --paper: #ffffff;
    --water-deep: #1a7fc2;
    --water-mid: #4fb0e2;
    --water-light: #9fd6f1;
    --water-pale: #dff1fa;
    --title-green: #3fc91c;
    --title-green-light: #8ee62c;
    --title-yellow: #fff200;
    --title-ink: #17300c;
    --gold-dark: #8a6412;
    --gold: #c9972b;
    --gold-light: #f3d67a;
    --badge-yellow: #ffe600;
    --badge-ink: #2f6f1c;
  }
  * { margin: 0; padding: 0; box-sizing: border-box; }
  html, body {
    width: 1200px;
    height: 501px;
    overflow: hidden;
    background: var(--paper);
  }
  .label {
    position: relative;
    width: 1200px;
    height: 501px;
    background: var(--frame-cyan);
    padding: 16px;
  }
  .label__artwork {
    position: relative;
    width: 100%;
    height: 100%;
    overflow: hidden;
    background: var(--paper);
  }
  .label__water {
    position: absolute;
    inset: 0;
    width: 100%;
    height: 100%;
  }
  .label__slogan {
    position: absolute;
    left: 0;
    right: 0;
    top: 34px;
    text-align: center;
    font-family: "Ultra", "Rockwell Extra Bold", serif;
    font-weight: 400;
    font-size: 56px;
    line-height: 74px;
    letter-spacing: 1px;
    color: var(--title-green);
    text-shadow:
      2px 2px 0 var(--title-yellow), -2px -2px 0 var(--title-yellow),
      2px -2px 0 var(--title-yellow), -2px 2px 0 var(--title-yellow),
      0 3px 0 var(--title-yellow), 0 -3px 0 var(--title-yellow),
      3px 0 0 var(--title-yellow), -3px 0 0 var(--title-yellow),
      4px 4px 0 var(--title-ink);
  }
  .label__slogan-line { display: block; white-space: nowrap; }
  .label__slogan-line--first { margin-left: -38px; }
  .label__slogan-line--second { margin-left: 86px; }
  .label__initial {
    font-family: "Lobster", cursive;
    font-size: 84px;
    color: var(--title-green-light);
    vertical-align: -4px;
  }
  .label__product {
    position: absolute;
    left: 0;
    right: 0;
    top: 236px;
    text-align: center;
  }
  .label__category {
    font-family: "Cinzel", serif;
    font-weight: 600;
    font-size: 34px;
    letter-spacing: 8px;
    background: linear-gradient(180deg, var(--gold-light) 0%, var(--gold) 55%, var(--gold-dark) 100%);
    -webkit-background-clip: text;
    background-clip: text;
    color: transparent;
    filter: drop-shadow(0 1px 0 rgba(255,255,255,0.8));
  }
  .label__rule {
    width: 260px;
    height: 2px;
    margin: 8px auto 10px;
    background: linear-gradient(90deg, transparent, var(--gold) 20%, var(--gold-light) 50%, var(--gold) 80%, transparent);
  }
  .label__name {
    font-family: "Cormorant Garamond", serif;
    font-style: italic;
    font-weight: 500;
    font-size: 30px;
    color: var(--paper);
    text-shadow: 0 1px 2px rgba(10, 60, 100, 0.6);
  }
  .label__brand {
    position: absolute;
    left: 1057px;
    top: 357px;
    width: 50px;
    height: 63px;
    background: var(--badge-yellow);
    display: flex;
    align-items: flex-end;
    justify-content: center;
    padding-bottom: 5px;
    font-family: "Nunito", sans-serif;
    font-weight: 800;
    font-size: 8px;
    color: var(--badge-ink);
  }
</style>
</head>
<body>
  <main class="label">
    <div class="label__artwork">
      <svg class="label__water" viewBox="0 0 1168 469" preserveAspectRatio="none" role="img" aria-label="Flowing blue water wave with splashes and droplets">
        <defs>
          <linearGradient id="wave-band" x1="0" y1="0" x2="1" y2="1">
            <stop offset="0" stop-color="#4fb0e2"/>
            <stop offset="0.5" stop-color="#1a7fc2"/>
            <stop offset="1" stop-color="#4fb0e2"/>
          </linearGradient>
          <linearGradient id="wave-low" x1="0" y1="0" x2="0" y2="1">
            <stop offset="0" stop-color="#9fd6f1"/>
            <stop offset="1" stop-color="#dff1fa"/>
          </linearGradient>
        </defs>
        <path d="M0 40 C200 60 360 150 560 240 C760 320 960 340 1168 250 L1168 469 L0 469 Z" fill="url(#wave-band)" opacity="0.85"/>
        <path d="M0 170 C240 200 420 300 640 360 C840 410 1000 380 1168 330 L1168 469 L0 469 Z" fill="url(#wave-low)"/>
        <path d="M0 300 C260 330 520 420 1168 410 L1168 469 L0 469 Z" fill="#bfe3f5"/>
        <path d="M0 20 C220 40 380 140 580 225 C780 305 970 320 1168 235" fill="none" stroke="#ffffff" stroke-width="3" opacity="0.7"/>
      </svg>
      <h1 class="label__slogan">
        <span class="label__slogan-line label__slogan-line--first"><span class="label__initial">G</span>Rown With Water</span>
        <span class="label__slogan-line label__slogan-line--second">and Sun</span>
      </h1>
      <div class="label__product">
        <p class="label__category">FLORAL WATER</p>
        <div class="label__rule"></div>
        <p class="label__name">Salvia Officinalis</p>
      </div>
      <div class="label__brand">tv lumora</div>
    </div>
  </main>
</body>
</html>
```